Luxury Business Card Design for High-End Window Treatments

Gilded Vantages
Custom Plantation Shutters & Architectural Shading Systems

⸻

BACK

Daniel Forsythe
Owner

Custom Interior & Exterior Window Treatments

919-482-7034
gildedvantages.com

I have included a picture that I’m hoping we can use on the back, but I’m also wondering if you can get rid of the ladder? Should we get rid of shutters , shades and blinds underneath Gilded Vantages?

Target Market(s)

High-end residential homeowners, custom home builders, architects, interior designers, and luxury renovation clients seeking premium plantation shutters and motorized architectural shading systems.

Industry/Entity Type

Custom Window treatments

Contact Information for Business Card

Front Gilded Vantages Custom Plantation Shutters Motorized Architectural Shading Systems BACK Daniel Forsythe Owner 919-482-7034 GildedVantages.com Custom Interior & Exterior Window Treatments By Appointment

Requirements
Nice to have
• Not 100% sure on nice to halves or the color but you can definitely check out my website to get a better understanding of what I’m trying to do

```html
<!DOCTYPE html>
<html lang="en">
<head>
<meta charset="utf-8">
<title>Gilded Vantages – Business Card</title>
<link rel="stylesheet" href="https://fonts.googleapis.com/css2?family=Poppins:wght@400;500&display=swap">
<style>
  :root {
    --page: #ffffff;
    --ink: #000000;
    --gold: #d4af37;
    --photo-top: #556a86;
    --photo-mid: #3b404a;
    --photo-low: #2c3036;
    --night: rgba(24, 30, 44, 0.82);
    --panel: rgba(12, 14, 22, 0.72);
    --band: rgba(20, 22, 28, 0.78);
  }
  * { margin: 0; padding: 0; box-sizing: border-box; }
  html, body {
    width: 972px; height: 1200px; overflow: hidden;
    background: var(--page);
    font-family: "Poppins", sans-serif;
  }
  .sheet { position: relative; width: 972px; height: 1200px; }
  .card {
    position: absolute; left: 136px; width: 700px; height: 400px; overflow: hidden;
  }
  .card--front { top: 168px; background: var(--ink); }
  .card--back { top: 634px; }

  .brand-name {
    position: absolute; left: 0; right: 0; top: 62px;
    text-align: center; color: var(--gold);
    font-weight: 400; font-size: 100px; line-height: 1; letter-spacing: 1px;
  }
  .brand-rule {
    position: absolute; left: 99px; width: 503px; top: 336px;
    height: 1px; background: var(--gold);
  }
  .brand-tagline {
    position: absolute; left: 0; right: 0; top: 344px;
    text-align: center; color: var(--gold);
    font-size: 14.6px; font-weight: 400;
  }

  .photo {
    position: absolute; inset: 0;
    background: linear-gradient(180deg, var(--photo-top) 0%, var(--photo-mid) 50%, var(--photo-low) 100%);
  }
  .photo-frame {
    position: absolute; inset: 0;
    border: 30px solid var(--night);
  }
  .contact-panel {
    position: absolute; left: 167px; top: 81px; width: 367px; height: 237px;
    border: 2px solid var(--gold); background: var(--panel);
  }
  .person-name, .person-role, .contact-phone, .contact-web {
    position: absolute; left: 0; right: 0; text-align: center; color: var(--gold);
  }
  .person-name { top: 100px; font-size: 40px; font-weight: 500; line-height: 1; }
  .person-role { top: 144px; font-size: 20px; font-weight: 400; line-height: 1; }
  .contact-phone { top: 251px; font-size: 21px; line-height: 1; }
  .contact-web { top: 277px; font-size: 21px; line-height: 1; }
  .service-band {
    position: absolute; left: 0; right: 0; bottom: 0; height: 30px;
    background: var(--band); color: var(--gold);
    text-align: center; font-size: 15px; line-height: 32px;
  }
</style>
</head>
<body>
<main class="sheet">
  <section class="card card--front">
    <h1 class="brand-name">Gilded<br>Vantages</h1>
    <div class="brand-rule"></div>
    <p class="brand-tagline">Custom Plantation Shutters Motorized Architectural Shading Systems</p>
  </section>

  <section class="card card--back">
    <div class="photo" role="img" aria-label="Photo of a two-storey home with dark motorized exterior shades on the covered upper porch, white columns and trees against a blue sky"></div>
    <div class="photo-frame"></div>
    <div class="contact-panel"></div>
    <h2 class="person-name">Daniel Forsythe</h2>
    <p class="person-role">OWNER</p>
    <p class="contact-phone">919-482-7034</p>
    <p class="contact-web">GildedVantages.com</p>
    <p class="service-band">Custom Interior &amp; Exterior Window Treatments By Appointment</p>
  </section>
</main>
</body>
</html>
```